BrivoPeak Business Card Design Project

We are looking for a modern, clean business card design for our new company. We are a consulting firm focused on the financial services market providing management and IT consulting to banks, insurance companies, etc. Please include our company logo and company contact information from the attached file in the design. Two versions of the logo are attached, either version is acceptable. Logos are available in other file formats if needed. We would like to include the contact information for both our UK and US offices as well as the following information for each individual card holder: Name, position/title, address, phone number and e-mail address.
Updates
Project Deadline Extended
Reason: A last minute trip over seas has prevented us from finalizing the decision. A decision will be made this week. We apologize for the inconvenience.
Industry/Entity Type
Business
Contact Information for Business Card
Company logo.
Company locations and phone numbers for both the US and UK offices.
Company URL.
Cardholder Name
Cardholder Position/title
Cardholder Address
Cardholder Phone Number
Cardholder e-mail Address
Look and feel
Each slider illustrates characteristics of the customer's brand and the style your logo design should communicate.

```html
<!DOCTYPE html>
<html lang="en">
<head>
<meta charset="utf-8">
<title>BrivoPeak Partners – Business Card</title>
<link rel="stylesheet" href="https://fonts.googleapis.com/css2?family=Open+Sans:wght@400;700&display=swap">
<style>
  :root {
    --backdrop: #262626;
    --card-light: #9a9a9a;
    --card-dark: #6c6c6c;
    --brand-navy: #1e3866;
    --ink-light: #ffffff;
    --shadow: rgba(0,0,0,0.55);
  }
  * { margin: 0; padding: 0; box-sizing: border-box; }
  html, body { width: 1200px; height: 802px; overflow: hidden; }
  body {
    background: var(--backdrop);
    font-family: "Open Sans", sans-serif;
    display: flex;
    align-items: center;
    justify-content: center;
    gap: 40px;
  }
  .card {
    position: relative;
    width: 520px;
    height: 297px;
    border-radius: 2px;
    background: radial-gradient(ellipse at 50% 25%, var(--card-light), var(--card-dark) 85%);
    box-shadow: 0 14px 30px var(--shadow);
    color: var(--ink-light);
  }
  .brand-name {
    font-weight: 700;
    color: var(--brand-navy);
    white-space: nowrap;
    display: flex;
    align-items: center;
  }
  .brand-mark {
    display: inline-block;
    background: var(--brand-navy);
  }
  .card-front .brand-name {
    position: absolute;
    left: 50%; top: 50%;
    transform: translate(-50%, -50%);
    font-size: 40px;
    gap: 14px;
  }
  .card-front .brand-mark { width: 30px; height: 30px; }
  .card-back .brand-name {
    position: absolute;
    left: 150px; top: 34px;
    font-size: 20px;
    gap: 8px;
  }
  .card-back .brand-mark { width: 16px; height: 16px; }

  .holder {
    position: absolute;
    right: 34px; top: 88px;
    text-align: right;
    font-size: 12px;
    line-height: 1.55;
  }
  .holder-name { font-size: 16px; line-height: 1.1; }
  .holder-title { font-size: 10px; margin-bottom: 14px; }
  .holder-line { display: flex; justify-content: flex-end; align-items: center; gap: 8px; }
  .holder-line .icon-slot { width: 14px; display: inline-flex; justify-content: center; }
  .holder-address { padding-right: 22px; }

  .offices {
    position: absolute;
    left: 26px; bottom: 30px;
    font-size: 12px;
    line-height: 1.45;
  }
  .office { display: flex; gap: 12px; }
  .office + .office { margin-top: 14px; }
  .office-icons {
    display: flex; flex-direction: column; justify-content: flex-end;
    gap: 6px; padding-bottom: 2px;
  }
  .icon { width: 12px; height: 12px; fill: var(--ink-light); }
</style>
</head>
<body>

  <section class="card card-front" aria-label="Card front">
    <div class="brand-name"><span class="brand-mark"></span>BrivoPeak Partners</div>
  </section>

  <section class="card card-back" aria-label="Card back">
    <div class="brand-name"><span class="brand-mark"></span>BrivoPeak Partners</div>

    <div class="holder">
      <div class="holder-name">Evan Marlow</div>
      <div class="holder-title">Founder</div>
      <div class="holder-line">0431 907 265
        <span class="icon-slot"><svg class="icon" viewBox="0 0 12 12"><path d="M1 4c0-2 2-2.5 5-2.5S11 2 11 4v1H8.5V4h-5v1H1zM2.5 6h7l1 5h-9z"/></svg></span>
      </div>
      <div class="holder-line">cardholder@brivopeak.com
        <span class="icon-slot"><svg class="icon" viewBox="0 0 12 12"><path d="M0.5 2.5h11v7h-11z M1.5 3.5l4.5 3.5 4.5-3.5" fill="none" stroke="#fff" stroke-width="1"/></svg></span>
      </div>
      <div class="holder-line">99 demo street, demo place
        <span class="icon-slot"><svg class="icon" viewBox="0 0 12 12"><path d="M6 1l5.5 5H10v5H7.5V8h-3v3H2V6H.5z"/></svg></span>
      </div>
      <div class="holder-address">P.O. Box 000, 0000 Lacus, Avenue</div>
    </div>

    <div class="offices">
      <div class="office">
        <div class="office-icons">
          <svg class="icon" viewBox="0 0 12 12"><path d="M1 4c0-2 2-2.5 5-2.5S11 2 11 4v1H8.5V4h-5v1H1zM2.5 6h7l1 5h-9z"/></svg>
          <svg class="icon" viewBox="0 0 12 12"><path d="M6 1l5.5 5H10v5H7.5V8h-3v3H2V6H.5z"/></svg>
        </div>
        <div>UK: +44 7700 418 552<br>14 Harlow Mews<br>London, E2 9QT, Great Britain</div>
      </div>
      <div class="office">
        <div class="office-icons">
          <svg class="icon" viewBox="0 0 12 12"><path d="M1 4c0-2 2-2.5 5-2.5S11 2 11 4v1H8.5V4h-5v1H1zM2.5 6h7l1 5h-9z"/></svg>
          <svg class="icon" viewBox="0 0 12 12"><path d="M6 1l5.5 5H10v5H7.5V8h-3v3H2V6H.5z"/></svg>
        </div>
        <div>US: (555) 214- 3870<br>218 N Cedar Row, Suite 402<br>Millbrook UT 84990, United States</div>
      </div>
    </div>
  </section>

</body>
</html>
```